Business Card - Rebranding for Consulting Firm

We are renaming and rebranding our consulting firm and need to raise the level of quality of our cards as part of that effort. We consult to leading high tech, life science and other innovation sector companies.

Need a two-sided business card design.

Side 1: (a) Company logo (b) tag line: Invest Wisely in Your People (c) Name (d) Title (e) Phone 1: Office (f) Phone 2: Mobile (g) email: person@HollowmereAdvisory.com

Side 2: Two lines of text: (a) Growth is Imperative. Change is Constant. Talent Executes Strategy. (b) We help you excel at all three.

Target Market(s)

Business and human resources executives and senior managers

Industry/Entity Type

Management Consulting

Contact Information for Business Card

Font styles to use
Sans Serif

Requirements
Must have
• clean, not too busy, but with a bit of creativity. Stick to the colors used in the attached logo
• appeal to high tech, life science companies
Nice to have
• prefer white background

```html
<!DOCTYPE html>
<html lang="en">
<head>
<meta charset="utf-8">
<title>Hollowmere Advisory – Business Card</title>
<link rel="stylesheet" href="https://fonts.googleapis.com/css2?family=Questrial&family=Montserrat:wght@300;400;700&family=Open+Sans:wght@400&family=Roboto+Slab:wght@400&display=swap">
<style>
  :root {
    --page-bg: #f4f5f7;
    --card-bg: #fafafa;
    --brand-blue: #0b5f96;
    --brand-sky: #1d8fd0;
    --ink: #222222;
    --ink-soft: #444a50;
    --shadow: rgba(0, 0, 0, 0.14);
  }
  * { box-sizing: border-box; margin: 0; padding: 0; }
  html, body { width: 1200px; height: 900px; overflow: hidden; }
  body { background: var(--page-bg); position: relative; }
  .card {
    position: absolute;
    left: 250px;
    width: 700px;
    height: 400px;
    background: linear-gradient(135deg, #ffffff 0%, var(--card-bg) 55%, #ececec 100%);
    box-shadow: 0 6px 22px var(--shadow);
    overflow: hidden;
  }

  /* Back side */
  .card-back { top: 35px; }
  .statement {
    position: absolute;
    top: 140px;
    left: 0;
    width: 100%;
    text-align: center;
    font-family: "Questrial", sans-serif;
  }
  .statement-main { font-size: 21px; color: var(--ink-soft); letter-spacing: 0.3px; }
  .statement-sub { margin-top: 8px; font-size: 21px; color: var(--brand-blue); letter-spacing: 0.3px; }
  .band {
    position: absolute;
    left: 0;
    bottom: 0;
    width: 100%;
    height: 62px;
    background: var(--brand-blue);
  }

  /* Front side */
  .card-front { top: 465px; }
  .brand {
    position: absolute;
    top: 50px;
    right: 48px;
    text-align: right;
  }
  .brand-name {
    display: flex;
    align-items: center;
    justify-content: flex-end;
    gap: 12px;
    font-family: "Montserrat", sans-serif;
    font-weight: 400;
    font-size: 38px;
    color: var(--brand-blue);
    letter-spacing: -0.5px;
  }
  .brand-mark { width: 22px; height: 22px; background: var(--brand-sky); }
  .tagline {
    margin-top: 10px;
    font-family: "Open Sans", sans-serif;
    font-size: 18px;
    color: var(--ink-soft);
  }
  .identity {
    position: absolute;
    top: 150px;
    left: 48px;
    padding-left: 18px;
    border-left: 8px solid var(--brand-blue);
  }
  .person-name {
    font-family: "Montserrat", sans-serif;
    font-weight: 300;
    font-size: 28px;
    color: var(--ink);
    line-height: 1.1;
  }
  .person-name b { font-weight: 700; }
  .job-title {
    margin-top: 4px;
    font-family: "Roboto Slab", serif;
    font-size: 20px;
    color: var(--brand-sky);
  }
  .contacts {
    position: absolute;
    left: 120px;
    bottom: 40px;
    list-style: none;
    font-family: "Open Sans", sans-serif;
    font-size: 17px;
    color: var(--ink);
  }
  .contacts li { display: flex; align-items: center; gap: 12px; margin-top: 6px; }
  .contacts svg { width: 18px; height: 18px; flex: none; }
</style>
</head>
<body>

<section class="card card-back" aria-label="Business card back">
  <div class="statement">
    <p class="statement-main">Growth is Imperative. Change is Constant. Talent Executes Strategy.</p>
    <p class="statement-sub">We help you excel at all three.</p>
  </div>
  <div class="band"></div>
</section>

<section class="card card-front" aria-label="Business card front">
  <div class="brand">
    <div class="brand-name"><span class="brand-mark"></span>Hollowmere Advisory</div>
    <p class="tagline">Invest Wisely in Your People</p>
  </div>

  <div class="identity">
    <p class="person-name">Your <b>Name</b></p>
    <p class="job-title">Job Title</p>
  </div>

  <ul class="contacts">
    <li>
      <svg viewBox="0 0 24 24" aria-hidden="true"><path fill="#0b5f96" d="M12 2a7 7 0 0 0-7 7c0 5 7 13 7 13s7-8 7-13a7 7 0 0 0-7-7zm0 9.5A2.5 2.5 0 1 1 12 6.5a2.5 2.5 0 0 1 0 5z"/></svg>
      <span>000 000 0000</span>
    </li>
    <li>
      <svg viewBox="0 0 24 24" aria-hidden="true"><path fill="#0b5f96" d="M2 8c3-4 17-4 20 0l-2 3-4-1V8H8v2l-4 1zM6 12h12l2 8H4zm6 2a2.5 2.5 0 1 0 0 5 2.5 2.5 0 0 0 0-5z"/></svg>
      <span>000 000 0000</span>
    </li>
    <li>
      <svg viewBox="0 0 24 24" aria-hidden="true" fill="none" stroke="#0b5f96" stroke-width="1.6"><circle cx="12" cy="12" r="9"/><ellipse cx="12" cy="12" rx="4" ry="9"/><path d="M3 12h18M5 7h14M5 17h14"/></svg>
      <span>person@HollowmereAdvisory.com</span>
    </li>
  </ul>
</section>

</body>
</html>
```